Window Perf design with eadership quotes

I am wanting to create a window perf that covers windows in a conference room. I have included a picture of the windows. Each window is 26 1/2 inches by 92 inches. I have also included several other pictures to give an example of how I would like the Quotes to look.

Some Quotes I would like to use
1. Your Future is created by what you do today not tomorrow.
2. The answer is Yes
3. People don't care how much you know until they know how much you care.
4. Treat employees like they make a difference and they will.
5. Don't follow the crowd, Let the crowd follow you.
6. Treat people as if they were what they ought to be , and help them become what they are capable of being.
7. Leadership is not a title, its a behavior. LIVE IT
8. We make a living by what we get, We make a life by what we give.
9. Success is not final, failure is not fatal: it is courage to continue that counts.
10. The best way to predict your future is to create it.
11. The supreme quality of leadership is Integrity.
12. Whatever you are, Be a good one

Quotes

• I am imore interested in how this looks rather than including all of the quotes. I also ant this to be a solid background design for privacy.

```html
<!DOCTYPE html>
<html lang="en">
<head>
<meta charset="utf-8">
<title>Window Perf – Making Ideas Happen</title>
<link rel="stylesheet" href="https://fonts.googleapis.com/css2?family=Anton&display=swap">
<style>
  :root {
    --ink: #040406;
    --signal-red: #ec1c24;
    --highlight-yellow: #ffe014;
    --paper-grey: #e6e7e9;
  }
  html, body {
    margin: 0;
    padding: 0;
    width: 1200px;
    height: 4166px;
    overflow: hidden;
    background: var(--ink);
  }
  .window-perf {
    position: relative;
    width: 1200px;
    height: 4166px;
    background: var(--ink);
    font-family: "Anton", "Impact", "Arial Narrow", sans-serif;
  }
  .quote {
    position: absolute;
    left: 74px;
    top: 1406px;
    margin: 0;
    font-weight: 400;
    display: flex;
    flex-direction: column;
    align-items: flex-start;
    gap: 31px;
  }
  .quote-line {
    display: flex;
    align-items: center;
    height: 200px;
    padding: 0 18px 0 31px;
    box-sizing: border-box;
    font-size: 212px;
    font-weight: 400;
    line-height: 1;
    letter-spacing: 0;
    word-spacing: 0.02em;
    text-transform: uppercase;
    white-space: nowrap;
  }
  .quote-line__text {
    display: block;
    text-box: trim-both cap alphabetic;
  }
  .quote-line--negation {
    background: var(--signal-red);
    color: var(--paper-grey);
  }
  .quote-line--affirmation {
    background: var(--highlight-yellow);
    color: var(--ink);
  }
</style>
</head>
<body>
  <main class="window-perf">
    <h1 class="quote">
      <span class="quote-line quote-line--negation"><span class="quote-line__text">It’s not</span></span>
      <span class="quote-line quote-line--negation"><span class="quote-line__text">about ideas.</span></span>
      <span class="quote-line quote-line--affirmation"><span class="quote-line__text">It’s about</span></span>
      <span class="quote-line quote-line--affirmation"><span class="quote-line__text">making</span></span>
      <span class="quote-line quote-line--affirmation"><span class="quote-line__text">ideas</span></span>
      <span class="quote-line quote-line--affirmation"><span class="quote-line__text">happen.</span></span>
    </h1>
  </main>
</body>
</html>
```